Flyer design for the Harvest Lantern Summit 2019 (HALSUM)

Design a flyer for our annual conference with basic information about the conference: conference logo and year, Conference name: Harvest Lantern Summit Location: Talbot Community Center (Downtown Portland)482 Wexley Street, Portland, ME 04109, Date: August 8th, 9th, 10th and 11th, 2019Start time 7:00PMI would like the following three words added to the flyer. These words describe the vision of the conference: Prophetic, Fire, Overflow,

Contact info:
Website: www.vostel.org
Phone: 207 555 3184
Email: contact@meadowcrest.org

Target Market(s)

Young adults living in the United States

Industry/Entity Type

Religious

Font styles to use
Sans Serif

Colors

Designer to choose colors to be used in the design.

Requirements
Must have
• HALSUM must logo standout, the reader should be able to take a quick look and find key info,
Should not have
• Cross image, church image

```html
<!DOCTYPE html>
<html lang="en">
<head>
<meta charset="utf-8">
<title>Harvest Lantern Summit 2019 – Flyer</title>
<link rel="stylesheet" href="https://fonts.googleapis.com/css2?family=Montserrat:ital,wght@0,600;0,700;1,800;1,900&family=Nunito:wght@800;900&display=swap">
<style>
  :root {
    --ink: #0a0b0d;
    --wine: #9b2a2b;
    --flame-red: #d9261c;
    --amber: #f7941d;
    --gold: #f6be0f;
    --ember: #e2491b;
    --brand-blue: #1577bf;
    --sky-blue: #0b7fd0;
    --cream: #fffbe6;
    --mist: #e3e3e1;
    --white: #ffffff;
  }
  * { margin: 0; padding: 0; box-sizing: border-box; }
  html, body { width: 1200px; height: 846px; overflow: hidden; background: var(--ink); }
  .flyer {
    position: relative;
    width: 1200px;
    height: 846px;
    overflow: hidden;
    font-family: "Nunito", "Montserrat", sans-serif;
    color: var(--white);
  }
  .frame { position: absolute; inset: 0; }

  .logo {
    position: absolute;
    left: 0; right: 0; top: 62px;
    text-align: center;
  }
  .logo-name {
    font-family: "Montserrat", sans-serif;
    font-weight: 600;
    font-size: 86px;
    line-height: 1;
    letter-spacing: 4px;
    color: var(--brand-blue);
  }
  .logo-year {
    display: flex;
    align-items: center;
    justify-content: center;
    gap: 14px;
    margin-top: 8px;
    font-family: "Montserrat", sans-serif;
    font-weight: 600;
    font-size: 38px;
    letter-spacing: 18px;
    color: var(--amber);
  }
  .logo-year::before, .logo-year::after {
    content: "";
    width: 104px; height: 3px;
    background: var(--amber);
  }
  .logo-year span { margin-right: -18px; }

  .title { position: absolute; left: 0; top: 230px; width: 1200px; height: 320px; }
  .title text { font-family: "Montserrat", sans-serif; font-style: italic; font-weight: 900; }

  .vision {
    position: absolute;
    left: 0; right: 0; top: 572px;
    text-align: center;
    font-family: "Montserrat", sans-serif;
    font-style: italic;
    font-weight: 800;
    font-size: 38px;
    letter-spacing: 6px;
    word-spacing: 26px;
    color: var(--mist);
  }

  .detail-row { position: absolute; display: flex; align-items: center; gap: 12px; }
  .label-box {
    position: relative;
    padding: 4px 10px;
    border: 1.5px solid var(--mist);
    font-weight: 900;
    color: var(--sky-blue);
    font-size: 27px;
    line-height: 1.3;
  }
  .label-box::after {
    content: "";
    position: absolute;
    inset: -5px 4px 5px -5px;
    border: 1.5px solid var(--mist);
  }
  .detail-value { font-weight: 900; font-size: 27px; letter-spacing: 0.5px; }
  .date-row { left: 410px; top: 630px; }
  .time-row { left: 446px; top: 752px; }
  .time-row .detail-value { font-size: 29px; }

  .venue { position: absolute; left: 282px; top: 688px; display: flex; gap: 28px; }
  .venue svg { margin-top: 4px; }
  .venue-text { font-weight: 800; font-size: 22px; line-height: 30px; letter-spacing: 0.4px; }
</style>
</head>
<body>
<main class="flyer">
  <svg class="frame" width="1200" height="846" viewBox="0 0 1200 846" aria-hidden="true">
    <defs>
      <linearGradient id="band-glow" x1="0" y1="0" x2="0" y2="1">
        <stop offset="0" stop-color="var(--gold)"/>
        <stop offset="0.45" stop-color="var(--amber)"/>
        <stop offset="1" stop-color="var(--ember)"/>
      </linearGradient>
    </defs>
    <rect class="frame-base" width="1200" height="846" fill="var(--wine)"/>
    <path class="frame-red-band" d="M60,0 Q-40,420 90,846 L1110,846 Q1260,420 1140,0 Z" fill="var(--flame-red)"/>
    <path class="frame-glow-band" d="M150,0 Q40,420 150,846 L1050,846 Q1225,420 1075,0 Z" fill="url(#band-glow)"/>
    <path class="frame-panel" d="M201,0 Q65,420 185,846 L1011,846 Q1170,420 1022,0 Z" fill="var(--ink)"/>
  </svg>

  <header class="logo">
    <div class="logo-name">HALSUM</div>
    <div class="logo-year"><span>2019</span></div>
  </header>

  <svg class="title" viewBox="0 230 1200 320" role="img" aria-label="Harvest Lantern Summit">
    <g text-anchor="middle" font-size="150" letter-spacing="-4">
      <text x="600" y="362" fill="var(--sky-blue)" stroke="var(--sky-blue)" stroke-width="34" stroke-linejoin="round">HARVEST</text>
      <text x="600" y="362" fill="var(--amber)" stroke="var(--white)" stroke-width="14" stroke-linejoin="round" paint-order="stroke">HARVEST</text>
      <text x="600" y="362" fill="var(--amber)" stroke="var(--ink)" stroke-width="3" paint-order="stroke">HARVEST</text>

      <text x="600" y="526" fill="var(--sky-blue)" stroke="var(--sky-blue)" stroke-width="34" stroke-linejoin="round">SUMMIT</text>
      <text x="600" y="526" fill="var(--amber)" stroke="var(--white)" stroke-width="14" stroke-linejoin="round" paint-order="stroke">SUMMIT</text>
      <text x="600" y="526" fill="var(--amber)" stroke="var(--ink)" stroke-width="3" paint-order="stroke">SUMMIT</text>
    </g>
    <g text-anchor="middle" font-size="64" letter-spacing="2">
      <text x="612" y="420" fill="var(--ember)" stroke="var(--ink)" stroke-width="10" stroke-linejoin="round" paint-order="stroke">LANTERN</text>
      <text x="612" y="420" fill="var(--ember)" stroke="var(--cream)" stroke-width="3" paint-order="stroke">LANTERN</text>
    </g>
  </svg>

  <p class="vision">PROPHETIC FIRE OVERFLOW</p>

  <div class="detail-row date-row">
    <span class="label-box">Date:</span>
    <span class="detail-value">August 8th - 11th, 2019</span>
  </div>

  <address class="venue" style="font-style: normal;">
    <svg width="26" height="42" viewBox="0 0 26 42" aria-hidden="true">
      <ellipse cx="13" cy="38" rx="12" ry="3" fill="#3a3a3a"/>
      <path d="M13,1 C5.5,1 1,6.5 1,12.5 C1,21 13,33 13,33 C13,33 25,21 25,12.5 C25,6.5 20.5,1 13,1 Z" fill="#e53329"/>
      <circle cx="13" cy="12.5" r="5" fill="var(--white)"/>
    </svg>
    <div class="venue-text">
      <div>Talbot Community Center (Downtown Portland)</div>
      <div>482 Wexley Street, Portland, ME 04109,</div>
    </div>
  </address>

  <div class="detail-row time-row">
    <span class="label-box">Time:</span>
    <span class="detail-value">7:00PM Daily</span>
  </div>
</main>
</body>
</html>
```